Tovesca Website

I need a website for a startup company that provides GIS (Geographic Information Services) staffing and products for local cities. Current website is www.tovescagroup.com

```html
<!DOCTYPE html>
<html lang="en">
<head>
<meta charset="utf-8">
<title>Tovesca Group</title>
<link href="https://fonts.googleapis.com/css2?family=Noticia+Text:wght@700&family=Roboto:wght@400;500;700&family=Poppins:wght@400&display=swap" rel="stylesheet">
<style>
:root{
  --ink:#2e3440;
  --dark:#2f343f;
  --text:#222;
  --muted:#555;
  --accent:#6a9cc6;
  --light:#eef0f3;
  --line:#cfd3d8;
  --white:#fff;
}
*{box-sizing:border-box;margin:0;padding:0}
html,body{width:1200px;height:3857px;overflow:hidden;background:var(--white);font-family:'Roboto',sans-serif;color:var(--text)}
.page{position:relative;width:1200px;height:3857px}
.abs{position:absolute}
.serif{font-family:'Noticia Text',serif;font-weight:700;letter-spacing:2px;color:var(--ink)}
.topbar{left:0;top:0;width:1200px;height:60px;background:var(--dark);border-radius:0 0 40px 40px;color:var(--white);font-size:13px}
.topbar .item{position:absolute;top:22px;display:flex;align-items:center;gap:8px}
.topbar b{font-weight:500;font-size:14px}
.topbar .sep{position:absolute;left:536px;top:16px;width:2px;height:28px;background:var(--white)}
.socials{display:flex;gap:7px}
.socials span{width:26px;height:26px;border-radius:50%;background:var(--white);display:block}
.topbar .socials{position:absolute;left:960px;top:17px}
.logo{left:108px;top:80px;font-size:32px}
.nav{left:598px;top:90px;display:flex;gap:34px;font-size:15px}
.nav a{color:var(--text);text-decoration:none;position:relative}
.nav a.active{font-weight:700}
.nav a.active::after{content:"";position:absolute;left:-8px;right:-8px;bottom:-12px;height:3px;background:var(--ink)}
.map{left:0;top:128px;width:1200px;height:464px;background:linear-gradient(135deg,#eceef0,#e2e5e9 60%,#f1ece2)}
.map-card{left:808px;top:290px;width:220px;height:130px;background:var(--white);border:3px solid var(--dark);border-radius:6px;text-align:center}
.map-card h4{background:var(--dark);color:var(--white);font-family:'Noticia Text',serif;font-size:15px;letter-spacing:1px;padding:8px 0}
.map-card p{font-size:14px;line-height:26px;padding-top:10px}
.search-panel{left:111px;top:506px;width:978px;height:136px;background:var(--dark);border-radius:6px;color:var(--white)}
.search-panel h5{position:absolute;left:29px;top:28px;font-size:16px;font-weight:500}
.field{position:absolute;top:61px;height:40px;border:1px solid var(--white);font-size:12px;padding:12px 18px}
.radius{position:absolute;left:529px;top:62px;font-size:13px}
.slider{position:absolute;left:529px;top:92px;width:220px;height:6px;background:var(--white);border-radius:3px}
.slider i{position:absolute;left:0;top:0;width:98px;height:6px;background:#52a08a;border-radius:3px}
.slider b{position:absolute;left:90px;top:-6px;width:18px;height:18px;border-radius:50%;background:#52a08a}
.btn-search{position:absolute;left:791px;top:61px;width:157px;height:40px;background:var(--white);color:var(--text);font-size:13px;display:flex;align-items:center;gap:14px;padding-left:20px}
.section-title{left:0;width:1200px;text-align:center;font-size:34px}
.underline{height:4px;background:var(--ink)}
.svc-title{font-size:31px}
.svc-list{list-style:none;font-size:16.5px;font-weight:500;text-transform:uppercase}
.svc-list li{height:51.4px;display:flex;align-items:flex-start;gap:14px}
.svc-list svg{margin-top:-2px}
.photo{border:6px solid var(--white);box-shadow:0 4px 16px rgba(0,0,0,.18)}
.about{left:0;top:2027px;width:1200px;height:443px;background:var(--light)}
.about p{position:absolute;left:60px;width:1080px;top:150px;text-align:center;font-size:16.5px;line-height:31px;color:var(--muted);letter-spacing:.3px}
.btn{background:var(--accent);color:var(--white);font-weight:700;font-size:17px;display:flex;align-items:center;justify-content:center;letter-spacing:.5px}
.loc-search{left:851px;top:2541px;width:202px;height:37px;border:1px solid #666;font-size:15px;padding:9px 16px}
.loc-go{left:1068px;top:2541px;width:36px;height:36px;background:var(--accent);display:flex;align-items:center;justify-content:center}
.arrow{top:2605px;width:27px;height:27px;border-radius:50%;display:flex;align-items:center;justify-content:center}
.card{top:2658px;width:241px;height:139px;box-shadow:0 10px 20px rgba(0,0,0,.25);color:var(--white);font-size:12px;font-weight:700;display:flex;align-items:center;justify-content:center;letter-spacing:.3px}
.contact-block{left:0;top:2885px;width:381px;height:515px;background:linear-gradient(160deg,#1d3248,#0f1c2b)}
.contact-circle{left:154px;top:2915px;width:456px;height:456px;border-radius:50%;border:8px solid var(--white);background:radial-gradient(circle at 50% 40%,#6f7d86,#3e5a3d 55%,#2b3b2a);box-shadow:0 4px 14px rgba(0,0,0,.3)}
.input{border:1px solid var(--line);font-family:'Poppins',sans-serif;font-size:13px;color:#888;padding:0 20px;display:flex;align-items:center}
.footer{left:0;top:3488px;width:1200px;height:369px;background:var(--dark);border-radius:70px 70px 0 0;color:var(--white)}
.footer .serif{color:var(--white)}
.fnav{position:absolute;left:0;width:1200px;top:200px;display:flex;justify-content:center;gap:30px;font-size:17px}
.fline{position:absolute;left:111px;top:250px;width:978px;height:1px;background:#8a8f98}
</style>
</head>
<body>
<div class="page">

<header>
  <div class="abs topbar">
    <div class="item" style="left:108px">
      <svg width="12" height="16" viewBox="0 0 12 16"><path d="M6 0a6 6 0 0 0-6 6c0 4.5 6 10 6 10s6-5.5 6-10a6 6 0 0 0-6-6zm0 8.5A2.5 2.5 0 1 1 6 3.5a2.5 2.5 0 0 1 0 5z" fill="#fff"/></svg>
      <b>LOCATION :</b> 480 N. Orchard Way #210 Brightvale, CA 90210
    </div>
    <div class="sep"></div>
    <div class="item" style="left:566px">
      <svg width="14" height="14" viewBox="0 0 24 24"><path d="M6.6 10.8a15 15 0 0 0 6.6 6.6l2.2-2.2c.3-.3.7-.4 1-.2 1.1.4 2.3.6 3.6.6.6 0 1 .4 1 1V20c0 .6-.4 1-1 1A17 17 0 0 1 3 4c0-.6.4-1 1-1h3.5c.6 0 1 .4 1 1 0 1.3.2 2.5.6 3.6.1.3 0 .7-.2 1z" fill="#fff"/></svg>
      <b>CALL US :</b> +1 555 014 2290
    </div>
    <div class="socials"><span></span><span></span><span></span><span></span></div>
  </div>
  <div class="abs logo serif">TOVESCA GROUP</div>
  <nav class="abs nav">
    <a class="active">Home</a><a>About Us</a><a>Our Services</a><a>Latest News</a><a>Contact Us</a>
  </nav>
</header>

<section>
  <div class="abs map" role="img" aria-label="Street map of the office neighbourhood"></div>
  <svg class="abs" style="left:772px;top:350px" width="18" height="24" viewBox="0 0 12 16"><path d="M6 0a6 6 0 0 0-6 6c0 4.5 6 10 6 10s6-5.5 6-10a6 6 0 0 0-6-6z" fill="#e53935"/><circle cx="6" cy="6" r="2" fill="#8b1a1a"/></svg>
  <div class="abs map-card"><h4>TOVESCA GROUP, LLC</h4><p>480 N. Orchard Way #210<br>Brightvale, CA 90210</p></div>
  <div class="abs search-panel">
    <h5>SEARCH YOUR LOCATION</h5>
    <div class="field" style="left:30px;width:199px">Search Area</div>
    <div class="field" style="left:271px;width:217px">All Location</div>
    <div class="radius">Radius: 105 Km</div>
    <div class="slider"><i></i><b></b></div>
    <div class="btn-search"><svg width="16" height="16" viewBox="0 0 16 16"><circle cx="6.5" cy="6.5" r="5" fill="none" stroke="#222" stroke-width="1.6"/><path d="M10.5 10.5L15 15" stroke="#222" stroke-width="1.6"/></svg>Search</div>
  </div>
</section>

<svg width="0" height="0" style="position:absolute">
  <defs><symbol id="pin" viewBox="0 0 12 20"><circle cx="6" cy="5.5" r="5.5" fill="#222"/><rect x="5" y="9" width="2" height="11" fill="#222"/><circle cx="4.3" cy="3.8" r="1.3" fill="#777"/></symbol></defs>
</svg>

<section>
  <h2 class="abs section-title serif" style="top:700px">OUR SERVICES</h2>
  <div class="abs underline" style="left:528px;top:756px;width:144px"></div>

  <h3 class="abs svc-title serif" style="left:108px;top:800px">GIS CONSULTING</h3>
  <ul class="abs svc-list" style="left:108px;top:870px">
    <li><svg width="12" height="20"><use href="#pin"/></svg>GIS Projects</li>
    <li><svg width="12" height="20"><use href="#pin"/></svg>Staffing Solutions</li>
    <li><svg width="12" height="20"><use href="#pin"/></svg>System Architecture Design</li>
    <li><svg width="12" height="20"><use href="#pin"/></svg>GIS Analysis</li>
    <li><svg width="12" height="20"><use href="#pin"/></svg>Demographics</li>
    <li><svg width="12" height="20"><use href="#pin"/></svg>Map Products</li>
  </ul>
  <div class="abs photo" style="left:601px;top:801px;width:488px;height:355px;background:linear-gradient(135deg,#5e7488,#b8c4cf 50%,#3c4f64)" role="img" aria-label="Team meeting in a glass-walled conference room"></div>

  <div class="abs photo" style="left:113px;top:1205px;width:488px;height:355px;background:radial-gradient(circle at 50% 45%,#c2533a,#2d6a9a 35%,#173752)" role="img" aria-label="Red location pin over a glowing city map"></div>
  <h3 class="abs svc-title serif" style="left:781px;top:1205px">GIS APPLICATIONS</h3>
  <ul class="abs svc-list" style="left:781px;top:1275px">
    <li><svg width="12" height="20"><use href="#pin"/></svg>Orvalith Online</li>
    <li><svg width="12" height="20"><use href="#pin"/></svg>Orvalith Enterprise</li>
    <li><svg width="12" height="20"><use href="#pin"/></svg>Dashboards</li>
    <li><svg width="12" height="20"><use href="#pin"/></svg>Experience Composer</li>
    <li><svg width="12" height="20"><use href="#pin"/></svg>Custom Widgets</li>
    <li><svg width="12" height="20"><use href="#pin"/></svg>Custom Javascript Apps</li>
  </ul>

  <h3 class="abs svc-title serif" style="left:108px;top:1682px">SPATIAL DATA SOLUTIONS</h3>
  <ul class="abs svc-list" style="left:108px;top:1752px">
    <li><svg width="12" height="20"><use href="#pin"/></svg>Spatial Data Cleanup</li>
    <li><svg width="12" height="20"><use href="#pin"/></svg>GIS Data Model Design/Review</li>
    <li><svg width="12" height="20"><use href="#pin"/></svg>Integrating With Other Systems</li>
  </ul>
  <div class="abs photo" style="left:601px;top:1605px;width:488px;height:355px;background:linear-gradient(135deg,#b9a78c,#dfe3e8 45%,#1f5aa8)" role="img" aria-label="Hands holding a tablet showing a data chart"></div>
</section>

<section class="abs about">
  <h2 class="abs section-title serif" style="top:66px">ABOUT US</h2>
  <p>We are an innovative team of geospatial experts with 25 years of experience in the field of GIS. We specialize<br>in providing results-driven GIS solutions for local government<br>and the private sector.</p>
  <div class="abs section-title serif" style="top:253px;font-size:40px">25 YEARS OF EXPERIENCE</div>
  <div class="abs btn" style="left:514px;top:328px;width:172px;height:45px">LEARN MORE</div>
</section>

<section>
  <h2 class="abs serif" style="left:93px;top:2533px;font-size:34px">LOCATIONS</h2>
  <div class="abs underline" style="left:93px;top:2590px;width:94px"></div>
  <div class="abs loc-search">Search</div>
  <div class="abs loc-go"><svg width="16" height="16" viewBox="0 0 16 16"><circle cx="6.5" cy="6.5" r="5" fill="none" stroke="#fff" stroke-width="2"/><path d="M10.5 10.5L15 15" stroke="#fff" stroke-width="2"/></svg></div>
  <div class="abs arrow" style="left:1040px;background:#999"><svg width="10" height="12"><path d="M7 1L2 6l5 5" fill="none" stroke="#fff" stroke-width="2"/></svg></div>
  <div class="abs arrow" style="left:1077px;background:var(--accent)"><svg width="10" height="12"><path d="M3 1l5 5-5 5" fill="none" stroke="#fff" stroke-width="2"/></svg></div>
  <div class="abs card" style="left:94px;background:linear-gradient(180deg,#8a7a68,#33404e)" role="img" aria-label="City skyline at dusk">NEW YORK CITY - UNITED STATES</div>
  <div class="abs card" style="left:351px;background:linear-gradient(180deg,#a08a72,#4a3a36)" role="img" aria-label="City street with clock tower">NEW YORK CITY - UNITED STATES</div>
  <div class="abs card" style="left:608px;background:linear-gradient(180deg,#7a6650,#2a2f38)" role="img" aria-label="Downtown skyline at sunset">NEW YORK CITY - UNITED STATES</div>
  <div class="abs card" style="left:865px;background:linear-gradient(180deg,#8aa0b8,#3e4a58)" role="img" aria-label="Financial district towers">NEW YORK CITY - UNITED STATES</div>
</section>

<section>
  <div class="abs contact-block" role="img" aria-label="Location pin over a digital map"></div>
  <div class="abs contact-circle" role="img" aria-label="Aerial view of highway interchanges at dusk"></div>
  <h2 class="abs serif" style="left:640px;top:2928px;font-size:34px">CONTACT US</h2>
  <div class="abs underline" style="left:640px;top:2980px;width:94px"></div>
  <div class="abs input" style="left:641px;top:3028px;width:212px;height:47px">First Name</div>
  <div class="abs input" style="left:904px;top:3028px;width:255px;height:47px">Last Name</div>
  <div class="abs input" style="left:641px;top:3102px;width:212px;height:47px">E-mail</div>
  <div class="abs input" style="left:904px;top:3102px;width:255px;height:47px">Phone</div>
  <div class="abs input" style="left:640px;top:3183px;width:520px;height:82px;align-items:flex-start;padding-top:14px">Message</div>
  <div class="abs btn" style="left:640px;top:3307px;width:173px;height:43px">SEND MESSAGE</div>
</section>

<footer class="abs footer">
  <div class="abs serif" style="left:0;width:1200px;top:56px;text-align:center;font-size:35px">TOVESCA GROUP</div>
  <div class="abs socials" style="left:536px;top:139px"><span></span><span></span><span></span><span></span></div>
  <div class="fnav"><span>Home</span><span>|</span><span>About Us</span><span>|</span><span>Our Services</span><span>|</span><span>Latest News</span><span>|</span><span>Contact Us</span></div>
  <div class="fline"></div>
  <div class="abs" style="left:0;width:1200px;top:272px;text-align:center;font-size:16px">Copyright © 2024 Tovescagroup. All rights reserved.</div>
  <div class="abs" style="left:0;width:1200px;top:321px;text-align:center;font-size:14px;word-spacing:2px">Privacy policy &nbsp;&nbsp;&nbsp; | &nbsp;&nbsp;&nbsp; Cookies policy</div>
</footer>

</div>
</body>
</html>
```